Email Banner: Pale Harbor

Need an email banner for https://pale-harbor.example/ much the same design for the attatched just using the logo and brand as the guidance.

Tagline should be "Essential Whitepapers for Business Professionals" or "Whitepapers featured from the most reputable companies in the industry"

It will be going on an email that looks like this:

https://mailvista.example/emails/preview/fullscreen/a17d3b2e-8c4f-4e1a-9b6d-f24e8a1c5d90

So dont make it to thick and clunky.

Target Market(s)

IT Proffesioanls

Industry/Entity Type

Information Technology

Logo Text

Essential Whitepapers for Business Professionals

Logo styles of interest
Abstract Logo
Font styles to use
Sans Serif

Colors
0054AA
0677BA
7BADD7
CADEEF
E8F1F8

Requirements
Must have
• Logo and colour scheme from the weblink provided: https://pale-harbor.example/

```html
<!DOCTYPE html>
<html lang="en">
<head>
<meta charset="utf-8">
<title>Pale Harbor – Email Banners</title>
<link href="https://fonts.googleapis.com/css2?family=Figtree:wght@400;500;600;700&display=swap" rel="stylesheet">
<style>
  :root {
    --page-bg: #ffffff;
    --panel-light: #e8f1f8;
    --brand-ink: #0a2540;
    --brand-mark: #0054aa;
    --accent-blue: #0677ba;
    --deep-blue: #003366;
    --core-blue: #0054aa;
    --sky-blue: #7badd7;
    --text-light: #ffffff;
  }
  * { box-sizing: border-box; margin: 0; padding: 0; }
  html, body { width: 1200px; height: 1200px; overflow: hidden; background: var(--page-bg); }
  body { position: relative; font-family: "Figtree", Arial, sans-serif; }

  .banner {
    position: absolute;
    left: 119px;
    width: 972px;
    height: 152px;
    overflow: hidden;
    background: var(--panel-light);
  }
  .banner--inline { top: 390px; }
  .banner--stacked { top: 666px; }

  .banner__shapes { position: absolute; inset: 0; width: 100%; height: 100%; }

  .brand {
    position: absolute;
    left: 0;
    top: 0;
    height: 152px;
    display: flex;
    align-items: center;
    color: var(--brand-ink);
    font-weight: 700;
  }
  .brand__dot { border-radius: 50%; background: var(--brand-mark); flex: none; }

  .banner--inline .brand { padding-left: 22px; gap: 16px; }
  .banner--inline .brand__dot { width: 48px; height: 48px; }
  .banner--inline .brand__name { font-size: 33px; letter-spacing: -0.3px; }

  .banner--stacked .brand { padding-left: 24px; gap: 22px; }
  .banner--stacked .brand__dot { width: 80px; height: 80px; }
  .banner--stacked .brand__name { font-size: 37px; line-height: 36px; letter-spacing: -0.3px; }
  .banner--stacked .brand__name span { display: block; }

  .tagline {
    position: absolute;
    left: 380px;
    top: 38px;
    color: var(--text-light);
    font-size: 27.5px;
    line-height: 36px;
    font-weight: 400;
  }
  .tagline strong { font-weight: 600; }

  .cta {
    position: absolute;
    right: 0;
    top: 0;
    width: 172px;
    height: 46px;
    line-height: 46px;
    text-align: center;
    padding-left: 14px;
    color: var(--text-light);
    font-size: 18px;
    font-weight: 700;
    letter-spacing: 0.3px;
  }
</style>
</head>
<body>

  <section class="banner banner--inline" aria-label="Pale Harbor banner, inline name">
    <svg class="banner__shapes" viewBox="0 0 972 152" preserveAspectRatio="none" aria-hidden="true">
      <defs>
        <linearGradient id="blueFadeA" x1="0" y1="0" x2="1" y2="0">
          <stop offset="0" stop-color="var(--deep-blue)"/>
          <stop offset="0.45" stop-color="var(--core-blue)"/>
          <stop offset="1" stop-color="var(--sky-blue)"/>
        </linearGradient>
      </defs>
      <polygon points="295,0 972,0 972,152 379,152" fill="url(#blueFadeA)"/>
      <polygon points="265,0 295,0 379,152 349,152" fill="var(--accent-blue)"/>
      <polygon points="799,0 972,0 972,46 823,46" fill="var(--accent-blue)"/>
    </svg>
    <div class="brand">
      <span class="brand__dot"></span>
      <span class="brand__name">Pale Harbor</span>
    </div>
    <p class="tagline">Essential Whitepapers<br>for <strong>Business Professionals</strong></p>
    <a class="cta">CLICK HERE</a>
  </section>

  <section class="banner banner--stacked" aria-label="Pale Harbor banner, stacked name">
    <svg class="banner__shapes" viewBox="0 0 972 152" preserveAspectRatio="none" aria-hidden="true">
      <defs>
        <linearGradient id="blueFadeB" x1="0" y1="0" x2="1" y2="0">
          <stop offset="0" stop-color="var(--deep-blue)"/>
          <stop offset="0.45" stop-color="var(--core-blue)"/>
          <stop offset="1" stop-color="var(--sky-blue)"/>
        </linearGradient>
      </defs>
      <polygon points="295,0 972,0 972,152 379,152" fill="url(#blueFadeB)"/>
      <polygon points="265,0 295,0 379,152 349,152" fill="var(--accent-blue)"/>
      <polygon points="799,0 972,0 972,46 823,46" fill="var(--accent-blue)"/>
    </svg>
    <div class="brand">
      <span class="brand__dot"></span>
      <span class="brand__name"><span>Pale</span><span>Harbor</span></span>
    </div>
    <p class="tagline">Essential Whitepapers<br>for <strong>Business Professionals</strong></p>
    <a class="cta">CLICK HERE</a>
  </section>

</body>
</html>
```